Exciting & Elegant Stationary Pack

Stationary consists of
1. Letter head / Envelope
2. Business Card
3. Invoice
4. 40x40mm sticker

Attached files;

1. Logo (Other formats available on request)
2. MS word Doc - For information and description of design
3. Website image (This will be our new website so use the colours so everything ties together)
4. Sample of stationary pack we like, but feel free to be creative

Target Market(s)

Home improvement

Industry/Entity Type

Construction

Other font styles liked:
• Leave up to designer - We like font used on (website attached image)

Requirements
Must have
• Please look at uploaded file of sample website and use colours
Nice to have
• Any type of business card design - eg. metal, die cut, embossed, etc...

```html
<!DOCTYPE html>
<html lang="en">
<head>
<meta charset="utf-8">
<title>Tilecraft Business Card</title>
<link rel="stylesheet" href="https://fonts.googleapis.com/css2?family=Arimo:wght@400;700&display=swap">
<style>
  :root {
    --page-bg: #e9e6e1;
    --card-white: #ffffff;
    --card-blue: #1f5a85;
    --card-blue-light: #2a6a98;
    --accent-orange: #f39a3a;
    --text-white: #ffffff;
    --text-soft: #dce8f1;
    --shadow: rgba(0, 0, 0, 0.22);
  }
  html, body {
    margin: 0;
    padding: 0;
    width: 1200px;
    height: 950px;
    overflow: hidden;
    background: var(--page-bg);
    font-family: "Arimo", Arial, sans-serif;
  }
  .canvas {
    position: relative;
    width: 1200px;
    height: 950px;
  }
  .card {
    position: absolute;
    width: 600px;
    height: 343px;
    border-radius: 4px;
    box-shadow: 0 10px 28px var(--shadow);
    overflow: hidden;
  }
  .card-front {
    left: 110px;
    top: 110px;
    background: var(--card-white);
  }
  .card-back {
    left: 490px;
    top: 470px;
    background: var(--card-blue);
  }
  .card-back .sheen {
    position: absolute;
    inset: 0;
    width: 100%;
    height: 100%;
  }
  .brand-front {
    position: absolute;
    left: 0;
    right: 0;
    top: 50%;
    transform: translateY(-50%);
    display: flex;
    align-items: center;
    justify-content: center;
    gap: 14px;
  }
  .brand-mark {
    width: 22px;
    height: 22px;
    background: var(--card-blue);
  }
  .brand-front .brand-name {
    font-weight: 700;
    font-size: 40px;
    letter-spacing: 2px;
    color: var(--card-blue);
  }
  .brand-back {
    position: absolute;
    left: 34px;
    top: 110px;
    font-weight: 700;
    font-size: 66px;
    letter-spacing: 3px;
    color: var(--text-white);
  }
  .contact-person {
    position: absolute;
    right: 34px;
    top: 118px;
    text-align: right;
    color: var(--text-white);
  }
  .contact-person .name {
    font-weight: 700;
    font-size: 19px;
  }
  .contact-person .role {
    font-size: 14px;
    color: var(--text-soft);
    margin-top: 4px;
  }
  .contact-details {
    position: absolute;
    right: 34px;
    bottom: 34px;
    text-align: right;
    color: var(--text-white);
    font-size: 14px;
    line-height: 1.7;
  }
</style>
</head>
<body>
<main class="canvas">
  <section class="card card-front" aria-label="Business card front">
    <div class="brand-front">
      <span class="brand-mark"></span>
      <span class="brand-name">TILECRAFT</span>
    </div>
  </section>

  <section class="card card-back" aria-label="Business card back">
    <svg class="sheen" viewBox="0 0 600 343" preserveAspectRatio="none" aria-hidden="true">
      <polygon points="0,230 600,40 600,343 0,343" fill="var(--card-blue-light)" opacity="0.35"/>
      <line x1="0" y1="230" x2="600" y2="40" stroke="#ffffff" stroke-opacity="0.12" stroke-width="1"/>
    </svg>
    <div class="brand-back">TILECRAFT</div>
    <div class="contact-person">
      <div class="name">Minh Tran</div>
      <div class="role">Project Manager</div>
    </div>
    <div class="contact-details">
      <div>Lic No. 204619c &nbsp;|&nbsp; M : 0400 318 752</div>
      <div>E : info@tilecraft.com.au &nbsp; W : www.tilecraft.com.au</div>
    </div>
  </section>
</main>
</body>
</html>
```